Flyer Design Project

I am starting a new Cake Business called "FROSTED HOUR" and want flyers. The main product are Cupcakes and will be marketed for parties/events/celebrations to order. Other cakes can be made to order (Christmas/Birthday etc)

Industry/Entity Type

Business

Requirements
Must have
• Contact Telephone Number

```html
<!DOCTYPE html>
<html lang="en">
<head>
<meta charset="utf-8">
<title>Frosted Hour – Cupcake Flyer</title>
<link href="https://fonts.googleapis.com/css2?family=Alegreya:wght@400&display=swap" rel="stylesheet">
<style>
  :root{
    --stage:#1e1e20;
    --sky:#a6d9f3;
    --band-top:#bfe0ea;
    --band-mid:#a9d3dc;
    --band-edge:#e2a3b4;
    --cream:#fbece2;
    --cream-border:#e4d5cb;
    --berry:#b12f68;
    --rose:#d57aa7;
    --photo-blue:#4aa8d8;
    --photo-pink:#e79ab4;
    --photo-choc:#4a2c22;
  }
  *{margin:0;padding:0;box-sizing:border-box}
  html,body{width:1200px;height:1000px;overflow:hidden;background:var(--stage)}
  .canvas{position:relative;width:1200px;height:1000px}
  .flyer{
    position:absolute;left:255px;top:25px;width:690px;height:950px;
    background:var(--sky);overflow:hidden;
  }
  .header-band{
    position:absolute;left:0;top:35px;width:100%;height:250px;
    background:linear-gradient(180deg,var(--band-edge) 0 6px,var(--band-top) 6px 40px,var(--band-mid) 40px 210px,var(--band-top) 210px 244px,var(--band-edge) 244px 250px);
  }
  .brand-title{
    position:absolute;left:0;top:112px;width:100%;text-align:center;
    font-family:"Alegreya",serif;font-weight:400;font-size:66px;
    letter-spacing:6px;color:var(--berry);line-height:1;
  }
  .photo{
    position:absolute;width:220px;height:220px;border-radius:50%;
    border:10px solid var(--cream);
  }
  .photo--blue{left:30px;top:300px;background:radial-gradient(circle at 50% 40%,var(--photo-blue),#6b4a3a 80%)}
  .photo--pink{left:235px;top:262px;background:radial-gradient(circle at 50% 45%,var(--photo-pink),#d8d2c2 80%)}
  .photo--choc{left:440px;top:225px;background:radial-gradient(circle at 50% 45%,#f2ead6,var(--photo-choc) 85%)}
  .info-panel{
    position:absolute;left:40px;top:545px;width:610px;height:360px;
    background:var(--cream);border:8px solid var(--cream-border);border-radius:34px;
    font-family:"Alegreya",serif;text-align:center;
  }
  .info-panel p{line-height:1.15}
  .lead{margin-top:34px;font-size:24px;color:var(--berry)}
  .occasions{font-size:36px;color:var(--rose)}
  .occasions .tail{font-size:24px;color:var(--berry)}
  .other{font-size:22px;color:var(--berry);margin-top:4px}
  .cta{font-size:34px;color:var(--rose);margin-top:8px}
  .phone{position:absolute;left:34px;bottom:34px;font-size:32px;color:var(--berry);text-align:left}
</style>
</head>
<body>
<div class="canvas">
  <div class="flyer">
    <div class="header-band" role="img" aria-label="Lace trimmed polka dot border band"></div>
    <h1 class="brand-title">FROSTED HOUR</h1>

    <div class="photo photo--blue" role="img" aria-label="Photo of a cupcake with blue frosting"></div>
    <div class="photo photo--pink" role="img" aria-label="Photo of a cupcake with pink swirled frosting"></div>
    <div class="photo photo--choc" role="img" aria-label="Photo of chocolate cupcakes with cream topping and cookies"></div>

    <section class="info-panel">
      <p class="lead">We are making delicious Cupcakes for</p>
      <p class="occasions">parties/events/celebrations <span class="tail">to order.</span></p>
      <p class="other">Other cakes can be made to order (Christmas/Birthday etc) !</p>
      <p class="cta">Contact us today!</p>
      <p class="phone">Phone no:</p>
    </section>
  </div>
</div>
</body>
</html>
```